Whitcombe Framing Works - Card Design

I am looking to use the logo designs that you already did for me to develop a business card. I would like the card to have a black background and be double sided. I want white and green logo and text. I have attached an inspiration photo of a look that I like. I would like to use the Vertical Logo attached to take up the full front side of the card. On the back where I have my name and information, I would like to have the horizontal logo or maybe even just the image of the 'A' and trees without the text. I am open, but I am looking for something clean and simple and I want the green to really pop! Additional files can be found under Design #: 40593216

Target Market(s)

Homeowners

Industry/Entity Type

Construction

Contact Information for Business Card

Name: Marcus Pellow, Title: Project Manager, Phone: 831.555.0147, Email: whitcombeframingworks@mailbarn.net, address: 418 Juniper Ln, Felton, CA 95092, Lic# 2046318

Colors
00AB8E
00BBA5
67D7C9
C6EFE9
E9F9F6

Requirements
Nice to have
• I would like to see the logos that I have already got from SketchHarbor, though I am open to new ones

```html
<!DOCTYPE html>
<html lang="en">
<head>
<meta charset="utf-8">
<title>Whitcombe Framing Works – Business Card</title>
<link rel="stylesheet" href="https://fonts.googleapis.com/css2?family=Montserrat:wght@400;500;700&display=swap">
<style>
  :root {
    --backdrop: #3a3a3a;
    --card-black: #1e1e1e;
    --brand-green: #3cc04a;
    --text-white: #ffffff;
    --text-soft: #e6e6e6;
  }
  * { box-sizing: border-box; margin: 0; padding: 0; }
  html, body {
    width: 1200px; height: 1200px; overflow: hidden;
    background: var(--backdrop);
    font-family: "Montserrat", sans-serif;
  }
  .canvas {
    width: 1200px; height: 1200px;
    display: flex; flex-direction: column; align-items: center; justify-content: center;
    gap: 60px;
  }
  .card {
    position: relative;
    width: 900px; height: 514px;
    background: var(--card-black);
    border-radius: 34px;
    box-shadow: 0 10px 30px rgba(0,0,0,.45);
  }
  /* contact side */
  .wordmark {
    position: absolute; top: 70px; left: 0; right: 0;
    display: flex; align-items: center; justify-content: center; gap: 14px;
  }
  .wordmark__dot {
    width: 22px; height: 22px; border-radius: 50%;
    background: var(--brand-green);
  }
  .wordmark__name {
    font-weight: 700; font-size: 40px; color: var(--text-white);
    letter-spacing: 1px; text-transform: uppercase;
  }
  .holder {
    position: absolute; left: 60px; bottom: 70px;
  }
  .holder__name {
    font-weight: 700; font-size: 34px; color: var(--brand-green);
    text-transform: uppercase; letter-spacing: .5px;
  }
  .holder__title {
    font-weight: 500; font-size: 22px; color: var(--text-white);
    text-transform: uppercase; margin-top: 6px;
  }
  .contact {
    position: absolute; right: 50px; top: 230px;
    list-style: none; color: var(--text-soft);
    font-size: 19px; line-height: 1.2;
  }
  .contact li { display: flex; align-items: center; gap: 12px; margin-bottom: 12px; }
  .contact__licence { padding-left: 0; }
  .contact svg { width: 22px; height: 22px; fill: var(--brand-green); flex: none; }
  /* logo side */
  .card--front { display: flex; align-items: center; justify-content: center; }
  .front-mark {
    display: flex; align-items: center; gap: 22px;
  }
  .front-mark__ring {
    width: 44px; height: 44px; border-radius: 50%;
    border: 5px solid var(--brand-green);
  }
  .front-mark__name {
    font-weight: 700; font-size: 52px; color: var(--text-white);
    text-transform: uppercase; letter-spacing: 1px; line-height: 1.1;
  }
</style>
</head>
<body>
<main class="canvas">
  <section class="card card--back" aria-label="Contact side">
    <div class="wordmark">
      <span class="wordmark__dot"></span>
      <span class="wordmark__name">Whitcombe Framing Works</span>
    </div>
    <div class="holder">
      <p class="holder__name">Marcus Pellow</p>
      <p class="holder__title">Project Manager</p>
    </div>
    <ul class="contact">
      <li class="contact__licence">Lic# 2046318</li>
      <li>
        <svg viewBox="0 0 24 24" aria-hidden="true"><path d="M6.6 10.8a15.1 15.1 0 0 0 6.6 6.6l2.2-2.2a1 1 0 0 1 1-.25 11.4 11.4 0 0 0 3.6.57 1 1 0 0 1 1 1V20a1 1 0 0 1-1 1A17 17 0 0 1 3 4a1 1 0 0 1 1-1h3.5a1 1 0 0 1 1 1c0 1.25.2 2.45.57 3.6a1 1 0 0 1-.25 1z"/></svg>
        831.555.0147
      </li>
      <li>
        <svg viewBox="0 0 24 24" aria-hidden="true"><path d="M2 5h20v14H2zm2 2v.5l8 5 8-5V7l-8 5z"/></svg>
        whitcombeframingworks@mailbarn.net
      </li>
      <li>
        <svg viewBox="0 0 24 24" aria-hidden="true"><path d="M12 2a7 7 0 0 0-7 7c0 5.2 7 13 7 13s7-7.8 7-13a7 7 0 0 0-7-7zm0 9.5A2.5 2.5 0 1 1 12 6.5a2.5 2.5 0 0 1 0 5z"/></svg>
        418 Juniper Ln, Felton, CA 95092
      </li>
    </ul>
  </section>

  <section class="card card--front" aria-label="Logo side">
    <div class="front-mark">
      <span class="front-mark__ring"></span>
      <span class="front-mark__name">Whitcombe<br>Framing Works</span>
    </div>
  </section>
</main>
</body>
</html>
```